Business Cards for Harbourline Coatings Pty Ltd

Hi every one i need a design for my buisness cards. I Want my logo in it and the name of the company needs to stand out Harbourline Coatings Pty Ltd. I want the background of the buisness cards black and i want the font to stand out in either a white or a silver stylish text. I want the design to be simple but original not to in your face if you know what i mean. I want on the back of the buisness cards to have the services that my buisness offers.
• Interior/Exterior
• Residential/Commercial
• Special effects/Texture Coatings
• Water Damage Repair
• Fully qualified
• Pensioner Discount
• 10 Year guarantee
• Fully Insured
• Obligation free quotes
full internal repaints include a proffesionla cleaning service
I want the services on the back to be layed out in an originall way not just dot points. If possible could my logo take up the whole back ground of the back but the text with the services be kind of like transparent so u cvan still see the logo i dont know if its possible it woiuld just look cool if possible. When i pick a design ill give my contact details to the designer to add to the design at the end. Any questions please just ask! Ill upload my logo.
Conatcs will include office phone: Mobile: E-mail - dale@harbourlinecoatings.com.au, Ill also have a Postal address which is a PO Box and my website is www.harbourlinecoatings.com.au

```html
<!DOCTYPE html>
<html lang="en">
<head>
<meta charset="utf-8">
<title>Harbourline Coatings – Business Cards</title>
<link rel="stylesheet" href="https://fonts.googleapis.com/css2?family=Questrial&family=Archivo:wght@600&display=swap">
<style>
  :root {
    --backdrop: #8a8580;
    --card: #050505;
    --white: #ffffff;
    --silver: #d9d9d9;
    --green: #8dc63f;
    --green-dark: #2f7d3a;
  }
  * { margin: 0; padding: 0; box-sizing: border-box; }
  html, body { width: 1200px; height: 900px; overflow: hidden; }
  body {
    background: var(--backdrop);
    position: relative;
    font-family: "Questrial", Arial, sans-serif;
    color: var(--white);
  }
  .card {
    position: absolute;
    top: 282px;
    width: 495px;
    height: 302px;
    background: var(--card);
    border-radius: 14px;
  }
  .card--front { left: 100px; }
  .card--back { left: 630px; }

  /* Front */
  .holder-name {
    position: absolute;
    left: 44px;
    top: 50px;
    font-size: 23px;
    letter-spacing: 0.2px;
  }
  .contact {
    position: absolute;
    left: 44px;
    top: 102px;
    list-style: none;
    font-size: 13.5px;
    line-height: 23px;
  }
  .contact .company { color: var(--green); font-weight: 400; }
  .contact .icon-row { display: flex; align-items: center; gap: 7px; }
  .contact svg { width: 11px; height: 11px; fill: none; stroke: var(--green); stroke-width: 1.6; }
  .brand-block {
    position: absolute;
    left: 300px;
    top: 72px;
    width: 150px;
    text-align: center;
  }
  .brand-square {
    display: block;
    width: 76px;
    height: 76px;
    margin: 0 auto 10px;
    background: var(--green);
  }
  .brand-name {
    font-size: 14px;
    letter-spacing: 1.5px;
    color: var(--white);
  }

  /* Back */
  .back-square {
    position: absolute;
    left: 212px;
    top: 58px;
    width: 72px;
    height: 72px;
    background: var(--green);
  }
  .back-title {
    position: absolute;
    left: 0; right: 0;
    top: 140px;
    text-align: center;
    font-family: "Archivo", Arial, sans-serif;
    font-weight: 600;
    font-size: 21px;
    color: var(--silver);
    letter-spacing: 0.3px;
  }
  .back-sub {
    position: absolute;
    left: 0; right: 0;
    top: 168px;
    text-align: center;
    font-family: "Archivo", Arial, sans-serif;
    font-weight: 600;
    font-size: 12px;
    color: var(--green);
  }
  .divider {
    position: absolute;
    left: 120px;
    top: 199px;
    width: 255px;
    height: 1px;
    background: linear-gradient(90deg, transparent, rgba(255,255,255,0.7), transparent);
  }
  .services {
    position: absolute;
    left: 0; right: 0;
    top: 208px;
    text-align: center;
    font-size: 11.2px;
    line-height: 21.5px;
  }
  .services .dot { color: var(--green); margin: 0 4px; }
</style>
</head>
<body>
  <section class="card card--front">
    <h1 class="holder-name" style="font-weight:400">Dale Merrick</h1>
    <ul class="contact">
      <li class="company">Harbourline Coatings Pty Ltd.</li>
      <li>Tidewater St. No 18 Marlow NSW</li>
      <li>PO BOX 48210</li>
      <li class="icon-row">
        <svg viewBox="0 0 12 12"><rect x="2" y="1" width="8" height="10" rx="1"/><path d="M4 4h4M4 7h4"/></svg>
        (02) 5550 1827
      </li>
      <li class="icon-row">
        <svg viewBox="0 0 12 12"><rect x="3" y="1" width="6" height="10" rx="1"/><path d="M5.5 9h1"/></svg>
        0400 555 318
      </li>
      <li class="icon-row">
        <svg viewBox="0 0 12 12"><rect x="1" y="2.5" width="10" height="7"/><path d="M1 2.5l5 4 5-4"/></svg>
        dale@harbourlinecoatings.com.au
      </li>
      <li class="icon-row">
        <svg viewBox="0 0 12 12"><circle cx="6" cy="6" r="4.8"/><path d="M1.2 6h9.6M6 1.2c-2.5 3-2.5 6.6 0 9.6M6 1.2c2.5 3 2.5 6.6 0 9.6"/></svg>
        www.harbourlinecoatings.com.au
      </li>
    </ul>
    <div class="brand-block">
      <span class="brand-square"></span>
      <span class="brand-name">HARBOURLINE</span>
    </div>
  </section>

  <section class="card card--back">
    <span class="back-square"></span>
    <h2 class="back-title">HARBOURLINE COATINGS</h2>
    <p class="back-sub">PTY LTD</p>
    <div class="divider"></div>
    <p class="services">
      Interior/Exterior<span class="dot">•</span>Residential/Commercial<span class="dot">•</span>Special effects/Texture Coatings<br>
      Water Damage Repair<span class="dot">•</span>Fully qualified<span class="dot">•</span>Pensioner Discount<span class="dot">•</span>10 Year guarantee<br>
      Fully Insured<span class="dot">•</span>Obligation free quotes
    </p>
  </section>
</body>
</html>
```